We are a doctors medical practice
I need the business card to be eye catching and memorable,
to reflect professionalism, yet also warmth and care

the numbers need to be easy to see, for the elderly

and the logo also in a location that is large enough to see and be eye catching

Back of card:
opening hours:
Mon- Fri 8.30am to 6pm
Sat 9am to 4pm

rows for appontments, date and time
Updates

HiĀ 

Modification to company name

BRAMBLEWOOD HOME HEALTH MEDICAL PRACTICE

Thanks
Clara

Reason: I am look for a unique design that also fulfils the design brief

I have attempted to post a .eps and .ai file of the logo

Target Market(s)

needs to appeal to the majority, mainly adults

Industry/Entity Type

Medical

Contact Information for Business Card

company name: Bramblewood Home Health Medical Practice
Name: Dr Clara Ostrowski-Vey
Qualifications: MBBS, Bsci(med), FRACGP, DCH, SH&FPA, Dip Derm
Address: Shop 3/41-43 Calder Rd, Brookvale 2371
Ph: 02 9418 3052
Fax: 02 9436 8120

Requirements
Nice to have
• I like balance
gold/ silver incorporated, as well as the other colours in the logo- but not limited to these colours
a "medical" feel
Should not have
• dark or strong colours

```html
<!DOCTYPE html>
<html lang="en">
<head>
<meta charset="utf-8">
<title>Bramblewood Home Health Medical Practice – Appointment Card</title>
<link rel="stylesheet" href="https://fonts.googleapis.com/css2?family=Tinos:wght@400;700&family=Arimo:wght@400&display=swap">
<style>
  :root {
    --ink: #111111;
    --frame: #000000;
    --paper: #ffffff;
    --stripe: #e4e4e4;
    --sky: #5a9ff0;
    --aqua: #4cc3ee;
    --ring: #2f8fe0;
    --ring-green: #7fd63a;
  }
  html, body {
    margin: 0;
    padding: 0;
    width: 1200px;
    height: 741px;
    overflow: hidden;
    background: var(--paper);
  }
  .card {
    position: relative;
    width: 1200px;
    height: 741px;
    background: var(--paper);
    font-family: "Tinos", "Times New Roman", serif;
    color: var(--ink);
  }
  .card__frame {
    position: absolute;
    left: 26px; top: 27px;
    width: 1150px; height: 686px;
    box-sizing: border-box;
    border: 9px solid var(--frame);
    background:
      repeating-linear-gradient(90deg,
        var(--paper) 0 8px,
        var(--stripe) 8px 10px);
  }
  .brand {
    position: absolute;
    left: 38px; top: 32px;
    width: 340px; height: 340px;
  }
  .brand__name {
    position: absolute;
    inset: 0;
    display: flex;
    align-items: center;
    justify-content: center;
    font-family: "Tinos", "Times New Roman", serif;
    font-size: 40px;
    color: var(--ink);
  }
  .practice-name {
    position: absolute;
    right: 92px; top: 80px;
    margin: 0;
    font-weight: 400;
    font-size: 38px;
    line-height: 1;
    white-space: nowrap;
  }
  .doctor-name {
    position: absolute;
    right: 92px; top: 128px;
    margin: 0;
    font-size: 38px;
    line-height: 1;
    white-space: nowrap;
  }
  .hours__title {
    position: absolute;
    left: 472px; top: 222px;
    width: 506px; height: 54px;
    border-top: 2px solid var(--ink);
    border-bottom: 2px solid var(--ink);
    box-sizing: border-box;
    font-family: "Arimo", Arial, sans-serif;
    font-size: 38px;
    color: var(--sky);
    text-align: center;
    line-height: 50px;
    word-spacing: 10px;
    margin: 0;
    font-weight: 400;
  }
  .hours__title::before,
  .hours__title::after {
    content: "";
    position: absolute;
    left: 0; right: 0;
    border-top: 2px solid var(--ink);
  }
  .hours__title::before { top: 4px; }
  .hours__title::after { bottom: 4px; }
  .hours__list {
    position: absolute;
    left: 380px; top: 286px;
    width: 694px;
    margin: 0; padding: 0;
    list-style: none;
    text-align: center;
    font-size: 38px;
    line-height: 42px;
  }
  .appointment {
    position: absolute;
    font-size: 48px;
    line-height: 1;
    white-space: nowrap;
  }
  .appointment__rule {
    display: inline-block;
    border-bottom: 2px solid var(--ink);
    vertical-align: baseline;
    height: 1px;
  }
  .appointment--date { left: 113px; top: 400px; }
  .appointment--date .appointment__rule { width: 550px; }
  .appointment--time { left: 391px; top: 481px; }
  .appointment--time .appointment__rule { width: 540px; margin-left: 12px; }
  .contact {
    position: absolute;
    top: 582px;
    height: 52px;
    box-sizing: border-box;
    border-top: 2px solid var(--ink);
    border-bottom: 2px solid var(--ink);
    font-size: 40px;
    color: var(--aqua);
    text-align: center;
    line-height: 52px;
  }
  .contact::before,
  .contact::after {
    content: "";
    position: absolute;
    left: 0; right: 0;
    border-top: 2px solid var(--ink);
  }
  .contact::before { top: 4px; }
  .contact::after { bottom: 4px; }
  .contact--fax {
    left: 84px; width: 508px;
    font-family: "Arimo", Arial, sans-serif;
    word-spacing: 14px;
  }
  .contact--phone { left: 603px; width: 508px; }
  .address {
    position: absolute;
    left: 70px; top: 640px;
    width: 1056px;
    margin: 0;
    font-style: normal;
    font-weight: 700;
    font-size: 48px;
    letter-spacing: 3px;
    word-spacing: 6px;
    text-align: center;
    white-space: nowrap;
  }
</style>
</head>
<body>
<main class="card">
  <div class="card__frame"></div>

  <div class="brand">
    <svg width="340" height="340" viewBox="0 0 340 340" aria-hidden="true">
      <circle cx="170" cy="170" r="158" fill="none" stroke="var(--ring)" stroke-width="10"/>
    </svg>
    <span class="brand__name">Bramblewood</span>
  </div>

  <h1 class="practice-name">Bramblewood Home Health Medical Practice</h1>
  <p class="doctor-name">Dr. Clara Ostrowski-Vey</p>

  <h2 class="hours__title">Hours Of Operation:</h2>
  <ul class="hours__list">
    <li>Monday - Friday : 8:30AM-6:00PM</li>
    <li>Saturday: 9:00AM - 4:00PM</li>
  </ul>

  <div class="appointment appointment--date">Appointment Date:<span class="appointment__rule"></span></div>
  <div class="appointment appointment--time">Time: <span class="appointment__rule"></span></div>

  <div class="contact contact--fax">FAX: 02 9436 8120</div>
  <div class="contact contact--phone">Ph: 02 9418 3052</div>

  <address class="address">3/41-43 Calder Rd. Brookvale 2371</address>
</main>
</body>
</html>
```